Tarrow Water Taxi and Transport Flyer

I need a business flyer for my new water taxi and freight transport business I have started here in Kodiak Alaska. Kodiak is a remote island in the middle of the gulf of Alaska. There are seven native villages around the island and Kodiak is the #2 fishing port in the United States. We also have the largest Coast Guard Base in the U.S.
My company will be providing water taxi and freight transport logistics to the villages and many hunting and fishing lodges as well as remote properties around the island.

I would like a business flyer that isn't status quo, something that stands out. I do like clean minimal designs but it needs to have the necessary contact info on it.

Target Market(s)

remote lodge / property owners, residents of the many villages around the island and anyone wanting to enjoy the great outdoors of Kodiak Alaska

Industry/Entity Type

Business

Colors
0355a3
0493ce
3277b5
9bcb3c
abd037
faa54b
f78f20
f37122
f68d4d

Requirements
Must have
• logo and necessary contact info
• Captain Morgan Haskell
• www.tarrowferrylink.com
• morgan@tarrowferrylink.com

```html
<!DOCTYPE html>
<html lang="en">
<head>
<meta charset="utf-8">
<title>Tarrow Water Taxi and Transport Flyer</title>
<link href="https://fonts.googleapis.com/css2?family=Oswald:wght@500;700&family=Open+Sans:wght@400;600;700&display=swap" rel="stylesheet">
<style>
  :root {
    --navy: #0b2f66;
    --blue: #0355a3;
    --sky: #0493ce;
    --mid: #3277b5;
    --orange: #f78f20;
    --orange-deep: #f37122;
    --orange-light: #faa54b;
    --ink: #2b2b2b;
    --white: #ffffff;
    --paper: #f7f9fb;
  }
  * { box-sizing: border-box; margin: 0; padding: 0; }
  html, body { width: 807px; height: 1200px; overflow: hidden; background: var(--white); }
  body { font-family: "Open Sans", Arial, sans-serif; color: var(--ink); }
  .flyer { position: relative; width: 807px; height: 1200px; background: var(--white); overflow: hidden; }

  .header { position: absolute; left: 40px; top: 36px; }
  .header__title { font-family: "Oswald", "Arial Narrow", sans-serif; font-weight: 700; font-size: 58px; line-height: 1; color: var(--sky); letter-spacing: 1px; }
  .header__subtitle { font-family: "Oswald", "Arial Narrow", sans-serif; font-weight: 500; font-size: 34px; color: var(--navy); margin-top: 4px; letter-spacing: 1px; }
  .header__tag { font-family: "Oswald", "Arial Narrow", sans-serif; font-weight: 500; font-size: 19px; color: var(--sky); margin-top: 10px; letter-spacing: 1px; }

  .hero-photo { position: absolute; left: 360px; top: 150px; width: 447px; height: 470px; background: linear-gradient(160deg, #cfe3f1 0%, #6fa7cf 45%, #2f6f97 75%, #5b6f7c 100%); }
  .hero-frame { position: absolute; left: 0; top: 150px; width: 807px; height: 520px; pointer-events: none; }

  .about { position: absolute; left: 0; top: 250px; width: 380px; height: 420px; background: linear-gradient(180deg, var(--orange-light) 0%, var(--orange) 55%, var(--orange-deep) 100%); padding: 70px 38px 0 40px; color: var(--white); }
  .about__label { position: absolute; left: 0; top: 18px; background: var(--navy); color: var(--white); font-family: "Oswald", sans-serif; font-weight: 700; font-size: 24px; padding: 4px 40px 4px 40px; letter-spacing: 1px; }
  .about p { font-size: 13px; line-height: 1.5; margin-bottom: 14px; }

  .band { position: absolute; left: 0; height: 44px; width: 440px; background: linear-gradient(90deg, var(--navy), var(--blue)); color: var(--white); font-family: "Oswald", sans-serif; font-weight: 700; font-size: 24px; letter-spacing: 1px; padding: 4px 40px; clip-path: polygon(0 0, 94% 0, 100% 50%, 94% 100%, 0 100%); }
  .band--offer { top: 690px; }
  .band--trip { top: 855px; }

  .offer__text { position: absolute; left: 40px; top: 748px; width: 470px; font-size: 13px; line-height: 1.55; }

  .logo { position: absolute; left: 560px; top: 730px; width: 220px; display: flex; align-items: center; gap: 12px; }
  .logo__mark { width: 40px; height: 40px; border-radius: 50%; background: var(--sky); flex: none; }
  .logo__name { font-family: "Oswald", sans-serif; font-weight: 700; font-size: 30px; color: var(--blue); line-height: 1; letter-spacing: 2px; }
  .logo__sub { position: absolute; left: 52px; top: 46px; font-size: 11px; font-weight: 600; color: var(--blue); letter-spacing: .5px; }

  .trip-list { position: absolute; top: 914px; width: 245px; list-style: none; font-size: 13px; font-weight: 600; line-height: 1.45; }
  .trip-list--left { left: 40px; }
  .trip-list--right { left: 300px; width: 230px; }
  .trip-list li { position: relative; padding-left: 16px; margin-bottom: 10px; }
  .trip-list li::before { content: ""; position: absolute; left: 0; top: 7px; width: 7px; height: 7px; border-radius: 50%; background: var(--sky); }

  .trip-photo { position: absolute; left: 560px; width: 220px; height: 105px; border: 3px solid var(--blue); }
  .trip-photo--deck { top: 870px; background: linear-gradient(135deg, #a9b4bc, #5f7383 60%, #3c4c58); }
  .trip-photo--cabin { top: 985px; background: linear-gradient(135deg, #c7cdd1, #8c8f8a 55%, #4e5a63); }

  .footer { position: absolute; left: 0; top: 1100px; width: 807px; height: 100px; background: linear-gradient(90deg, var(--navy), var(--blue)); color: var(--white); padding: 14px 40px; }
  .footer__captain { font-weight: 700; font-size: 14px; margin-bottom: 4px; }
  .contact { display: flex; align-items: center; gap: 8px; font-size: 12px; line-height: 1.55; }
  .contact svg { width: 12px; height: 12px; flex: none; }
</style>
</head>
<body>
<main class="flyer">
  <header class="header">
    <h1 class="header__title">PROVIDING WATER</h1>
    <p class="header__subtitle">TAXI &amp; FREIGHT TRANSPORT</p>
    <p class="header__tag">SERVICES TO THE KODIAK AREA</p>
  </header>

  <div class="hero-photo" role="img" aria-label="Photo of the aluminum catamaran landing craft cruising on open water"></div>
  <svg class="hero-frame" viewBox="0 0 807 520" aria-hidden="true">
    <polygon points="340,0 380,0 380,520 360,520" fill="#0493ce"/>
  </svg>

  <section class="about">
    <h2 class="about__label">ABOUT US</h2>
    <p>Tarrow Water Taxi and Transport is a locally owned and operated business providing water taxi services and freight transport in and around Kodiak Island.</p>
    <p>The vessel the Harbor Drift is a 33 foot long by 14 foot wide aluminum catamaran landing craft built in Sitka Alaska by Northline Marine in 2007.</p>
    <p>The catamaran hull design provides for one of the safest, most comfortable and capable hull designs that enhances the performance of the boat.</p>
  </section>

  <h2 class="band band--offer">WHAT WE OFFER</h2>
  <p class="offer__text">The Harbor Drift is capable of carrying up to 5,000 pounds and 6 passengers. Our vessel is equipped with extra large fuel tanks and powerful and fuel efficient outboards, allowing us to access all of Kodiak Island at a cruise speed between 20 and 24 miles per hour.</p>

  <div class="logo">
    <span class="logo__mark"></span>
    <span class="logo__name">TARROW</span>
    <span class="logo__sub">Water Taxi &amp; Transport</span>
  </div>

  <h2 class="band band--trip">EACH TRIP INCLUDES</h2>
  <ul class="trip-list trip-list--left">
    <li>Pick up or drop off to and from your location</li>
    <li>Comfortable cabin with heat, bathroom, efficient galley, surround sound stereo with blue tooth capability</li>
  </ul>
  <ul class="trip-list trip-list--right">
    <li>Large front deck for cargo or wild life viewing</li>
    <li>Some of the best customer service you will receive anywhere</li>
    <li>A knowledgeable and friendly captain</li>
  </ul>

  <div class="trip-photo trip-photo--deck" role="img" aria-label="Photo of the open front cargo deck of the boat"></div>
  <div class="trip-photo trip-photo--cabin" role="img" aria-label="Photo of the heated cabin interior"></div>

  <footer class="footer">
    <p class="footer__captain">Captain Morgan Haskell</p>
    <p class="contact"><svg viewBox="0 0 12 12"><path d="M2.5 1h2l1 3-1.3 1a6 6 0 0 0 2.8 2.8L8 6.5l3 1v2c0 .8-.7 1.5-1.5 1.5A9 9 0 0 1 1 2.5C1 1.7 1.7 1 2.5 1z" fill="#fff"/></svg>907-555-0148</p>
    <p class="contact"><svg viewBox="0 0 12 12"><rect x="1" y="2.5" width="10" height="7" rx="1" fill="#fff"/><path d="M1.5 3l4.5 3.5L10.5 3" stroke="#0355a3" fill="none"/></svg>morgan@tarrowferrylink.com</p>
    <p class="contact"><svg viewBox="0 0 12 12"><circle cx="6" cy="6" r="5" fill="none" stroke="#fff"/><path d="M1 6h10M6 1c2 2 2 8 0 10M6 1c-2 2-2 8 0 10" stroke="#fff" fill="none"/></svg>www.tarrowferrylink.com</p>
  </footer>
</main>
</body>
</html>
```